Develop a label for our product

We need a label design for our new company and new product. The total length of the label is 16 inches. However 4.5 inches is reserved for nutritional information. Consequently your area to work with is 11.5 length x 4.25
Attachment 1 is our logo.
Attachment 2 is a draft write-up about the product.
Attachment 3 is a draft write-up about us.
Attachment 4 is a picture of the container, this container is a larger version of the one we will be using,but the style, look and feel will be the same. This larger container size has a canvas size of 12 x 6.5.
Attachment/file 5 is the medium sized bottle.
Attachment 6 and 7 are the ai and psd file for the logo
We don't have a name select yet but here are the front runners:
Steady Frame Protein
Honestly Fine Protein Blend
Hazelbark Protein
Built with us Protein

Address is
TOVE BRAMBLE! LLC
718 Pellam Court
Dunmore Flats, PA 16340

WWW.TOVEBRAMBLE.net

This is our first time using pixelguild so please bear with us as we are learning.
We most likely will contract for additional work to include a 5 x 4 handout.

Target Market(s)

Athletes young and old
Health conscious individuals

Industry/Entity Type

It Company

Font styles to use
Sans Serif

Requirements
Must have
• Highlight "patent pending"
• 400mg cocoa flavanol
• all natural
• no additives or preservatives
• 3 ingredients
• A design which is simple and goes with our logo which is attached
Nice to have
• Able to be modified for future products.
Should not have
• Stock photo's.

```html
<!DOCTYPE html>
<html lang="en">
<head>
<meta charset="utf-8">
<title>Steady Frame Protein – Label</title>
<link rel="stylesheet" href="https://fonts.googleapis.com/css2?family=Ubuntu:wght@500;700&family=Arimo:wght@400;700&display=swap">
<style>
  :root{
    --stage:#3d3836;
    --kraft:#d8ae78;
    --kraft-light:#f3d6ac;
    --cocoa:#5a2d1b;
    --cocoa-mid:#7a4528;
    --cream:#fbefdc;
    --ink:#3b2216;
    --leaf-green:#3d9a3a;
    --stamp-red:#d2232a;
  }
  html,body{margin:0;padding:0;}
  body{
    width:1200px;height:900px;overflow:hidden;
    background:var(--stage);
    position:relative;
    font-family:"Arimo",Arial,sans-serif;
  }
  .label{position:absolute;left:0;top:0;width:1200px;height:900px;}
  .label svg{position:absolute;left:0;top:0;}
  .panel-copy{
    position:absolute;
    font-size:7.6px;line-height:10.2px;color:var(--ink);
    text-align:justify;
  }
  .panel-copy p{margin:0 0 9px;}
  .panel-copy .maker{font-weight:700;}
  .panel-copy .maker span{font-weight:400;display:block;}
  .panel-copy .web{font-weight:700;}
  .panel-left{left:88px;top:322px;width:250px;}
  .panel-right{left:866px;top:322px;width:247px;}
  .brand-name{
    position:absolute;left:492px;top:331px;
    display:flex;align-items:center;gap:8px;
    font-family:"Ubuntu",sans-serif;font-weight:700;font-size:25px;color:var(--cocoa);
  }
  .brand-name .dot{width:22px;height:22px;border-radius:50%;background:var(--cocoa);}
  .product-name{
    position:absolute;left:426px;top:424px;
    font-family:"Ubuntu",sans-serif;font-weight:700;font-size:18.5px;color:var(--cream);
  }
  .flavanol{
    position:absolute;left:492px;top:466px;
    font-size:10.5px;color:var(--ink);
  }
  .patent-stamp{
    position:absolute;left:536px;top:512px;
    transform:rotate(-17deg);
    border:2px solid var(--stamp-red);border-radius:3px;
    padding:1px 5px;background:var(--cream);
    font-family:"Arimo",sans-serif;font-weight:700;font-size:9px;line-height:9px;
    color:var(--stamp-red);text-align:center;
  }
</style>
</head>
<body>
<div class="label">
  <svg width="1200" height="900" viewBox="0 0 1200 900">
    <defs>
      <linearGradient id="emblemFill" x1="0" y1="0" x2="0" y2="1">
        <stop offset="0" stop-color="#ffffff"/>
        <stop offset="0.45" stop-color="#f4e4cf"/>
        <stop offset="1" stop-color="#dfb98c"/>
      </linearGradient>
      <linearGradient id="waveFill" x1="0" y1="0" x2="1" y2="0">
        <stop offset="0" stop-color="#e8cba6" stop-opacity="0"/>
        <stop offset="0.6" stop-color="#b58660" stop-opacity="0.45"/>
        <stop offset="1" stop-color="#e8cba6" stop-opacity="0"/>
      </linearGradient>
      <clipPath id="emblemClip">
        <path d="M470,318 C520,296 680,296 730,318 C735,335 735,360 722,378 C770,395 792,430 792,470 C792,525 705,565 600,565 C495,565 408,525 408,470 C408,430 430,395 478,378 C465,360 465,335 470,318 Z"/>
      </clipPath>
      <path id="badgeTop" d="M671,438 A44,44 0 0 1 759,438"/>
      <path id="badgeBottom" d="M665,438 A50,50 0 0 0 765,438"/>
    </defs>

    <!-- label strip -->
    <rect x="20" y="273" width="1160" height="307" fill="var(--kraft)"/>
    <rect x="20" y="273" width="1160" height="4" fill="var(--cocoa)"/>
    <rect x="20" y="576" width="1160" height="4" fill="var(--cocoa)"/>
    <rect x="20" y="280" width="1160" height="1" fill="var(--cocoa-mid)"/>
    <rect x="20" y="572" width="1160" height="1" fill="var(--cocoa-mid)"/>

    <!-- side panels -->
    <path class="panel" d="M62,292 H364 A14,14 0 0 0 378,306 V551 A14,14 0 0 0 364,565 H62 A14,14 0 0 0 48,551 V306 A14,14 0 0 0 62,292 Z" fill="var(--kraft-light)" stroke="var(--cocoa)" stroke-width="2"/>
    <path class="panel" d="M840,292 H1138 A14,14 0 0 0 1152,306 V551 A14,14 0 0 0 1138,565 H840 A14,14 0 0 0 826,551 V306 A14,14 0 0 0 840,292 Z" fill="var(--kraft-light)" stroke="var(--cocoa)" stroke-width="2"/>

    <!-- centre emblem -->
    <path d="M470,318 C520,296 680,296 730,318 C735,335 735,360 722,378 C770,395 792,430 792,470 C792,525 705,565 600,565 C495,565 408,525 408,470 C408,430 430,395 478,378 C465,360 465,335 470,318 Z" fill="url(#emblemFill)" stroke="var(--cocoa)" stroke-width="3"/>
    <g clip-path="url(#emblemClip)">
      <rect x="400" y="420" width="300" height="36" fill="var(--cocoa)"/>
      <rect role="img" aria-label="Flowing line wave decoration" x="560" y="455" width="180" height="85" fill="url(#waveFill)"/>
    </g>

    <!-- all natural seal -->
    <circle role="img" aria-label="All natural seal" cx="506" cy="516" r="20" fill="var(--leaf-green)" stroke="#ffffff" stroke-width="2"/>

    <!-- ingredients badge -->
    <circle cx="715" cy="438" r="57" fill="var(--cocoa-mid)" stroke="var(--cocoa)" stroke-width="3"/>
    <circle cx="715" cy="438" r="35" fill="var(--cream)"/>
    <circle role="img" aria-label="Jar with cocoa pods illustration" cx="715" cy="438" r="30" fill="#6b3a22"/>
    <text font-family="Ubuntu, sans-serif" font-weight="700" font-size="10" fill="var(--cream)" letter-spacing="0.5">
      <textPath href="#badgeTop" startOffset="50%" text-anchor="middle">HAZELBARK PROTEIN</textPath>
    </text>
    <text font-family="Ubuntu, sans-serif" font-weight="700" font-size="10" fill="var(--cream)" letter-spacing="0.5" dy="9">
      <textPath href="#badgeBottom" startOffset="50%" text-anchor="middle">3 INGREDIENTS</textPath>
    </text>
  </svg>

  <div class="panel-copy panel-left">
    <p class="maker">Manufactured by:<br>TOVE BRAMBLE! LLC<span>718 Pellam Court, Dunmore Flats, PA 16340</span></p>
    <p class="web">WWW.TOVEBRAMBLE.net</p>
    <p>Lorem ipsum dolor sit amet, consectetur adipiscing elit. Aenean eu nulla nec ipsum eleifend consectetur. Sed viverra nec tellus nec malesuada. Mauris quis tellus quis lacus auctor dignissim vel eu enim.</p>
    <p>Pellentesque suscipit magna at neque placerat viverra. Sed commodo eros vitae lorem lacinia facilisis. Nunc elementum libero vel massa consectetur, vel malesuada odio sagittis. Cras vehicula tristique est ac facilisis. Donec consequat rutrum ex sit amet maximus. Cras et dui lacus.</p>
    <p>Fusce semper pretium lacus, interdum varius libero condimentum vel. Nulla urna ipsum, vestibulum non imperdiet a, dictum sed est. Sed condimentum, purus vitae condimentum pharetra, justo nisi semper lacus, ac ultricies turpis massa non enim. Aenean dictum nisl vitae ornare luctus. Duis et libero nec justo rhoncus efficitur vel eget libero.</p>
  </div>

  <div class="panel-copy panel-right">
    <p>Pellentesque suscipit magna at neque placerat viverra. Sed commodo eros vitae lorem lacinia facilisis. Nunc elementum libero vel massa consectetur, vel malesuada odio sagittis. Cras vehicula tristique est ac facilisis. Donec consequat rutrum ex sit amet maximus. Cras et dui lacus. itae lorem lacinia facilisis. Nunc elementum libero</p>
    <p>Lorem ipsum dolor sit amet, consectetur adipiscing elit. Aenean eu nulla nec ipsum eleifend consectetur. Sed viverra nec tellus nec malesuada. Mauris quis tellus quis lacus auctor dignissim vel eu enim.</p>
    <p>Pellentesque suscipit magna at neque placerat viverra. Sed commodo eros vitae lorem lacinia facilisis. Nunc elementum libero vel massa consectetur, vel malesuada odio sagittis. Cras vehicula tristique est ac facilisis. Donec consequat rutrum ex sit amet maximus. Cras et dui lacus.</p>
    <p>Fusce semper pretium lacus, interdum varius libero condimentum vel. Nulla urna ipsum, vestibulum non imperdiet a, dictum sed est. Sed condimentum, purus vitae condimentum pharetra, justo nisi semper lacus, ac ultricies turpis massa non enim. Aenean dictum nisl vitae ornare luctus. Duis et libero nec justo rhoncus efficitur vel eget libero.</p>
  </div>

  <div class="brand-name"><span class="dot"></span>TOVE BRAMBLE!</div>
  <div class="product-name">Steady Frame Protein</div>
  <div class="flavanol">400mg cocoa flavanol</div>
  <div class="patent-stamp">PATENT<br>PENDING</div>
</div>
</body>
</html>
```